Invitation to Retail Shopping Event

-Must include logo
-Can contain product pictures depending on design
-I prefer any graphics to be my own product pictures
-Should include the following language:
Sip and Shop
Thursday, November 18
11 to 1 pm
478 Fenwick Lane
Come enjoy sips, snacks and shopping! Be the first to preview our new winter collection and get an early start on your holiday gifting.
Please RSVP to 402-319-5577 or info@pelbrika.com

```html
<!DOCTYPE html>
<html lang="en">
<head>
<meta charset="utf-8">
<title>Pelbrika Sip &amp; Shop Invitation</title>
<link rel="stylesheet" href="https://fonts.googleapis.com/css2?family=Arimo:wght@400;700&family=Parisienne&display=swap">
<style>
  :root {
    --page-bg: #ffffff;
    --blush: #ebd3cd;
    --footer-white: #fbfbfb;
    --logo-grey: #5e5e5e;
    --script-grey: #7a7a7a;
    --detail-rust: #8d4d3e;
    --invite-rose: #a96f63;
    --body-grey: #666666;
    --contact-grey: #555555;
    --tray-tone: #d9bf8c;
    --tray-dark: #4a3a2a;
    --gold-tone: #d6b55a;
    --slipper-pink: #e9a7a4;
    --slipper-cream: #f2e6dc;
    --slipper-lilac: #a9a2ad;
  }
  * { margin: 0; padding: 0; box-sizing: border-box; }
  html, body { width: 1200px; height: 1000px; overflow: hidden; background: var(--page-bg); }
  .canvas { position: relative; width: 1200px; height: 1000px; }
  .invitation {
    position: absolute; left: 284px; top: 20px; width: 638px; height: 958px;
    background: var(--blush); overflow: hidden;
    font-family: "Arimo", Arial, sans-serif;
  }
  .footer-band {
    position: absolute; left: 0; top: 816px; width: 100%; height: 142px;
    background: var(--footer-white);
  }
  .brand-name {
    position: absolute; left: 0; width: 638px; top: 112px; text-align: center;
    font-weight: 700; font-size: 50px; letter-spacing: 2px; color: var(--logo-grey);
  }
  .event-title {
    position: absolute; left: 121px; top: 278px; width: 400px; height: 80px;
    text-align: center; white-space: nowrap;
    font-family: "Parisienne", cursive; font-weight: 400; font-size: 60px; line-height: 80px;
    color: var(--script-grey);
    transform: rotate(-20deg); transform-origin: 50% 50%;
  }
  .event-details {
    position: absolute; left: 244px; width: 360px; top: 440px; text-align: center;
    font-size: 22px; line-height: 30px; color: var(--detail-rust);
  }
  .event-invite {
    position: absolute; left: 234px; width: 380px; top: 548px; text-align: center;
    font-size: 20px; line-height: 27px; color: var(--invite-rose);
  }
  .event-blurb {
    position: absolute; left: 20px; width: 330px; top: 676px; text-align: center;
    font-size: 20px; line-height: 27px; color: var(--body-grey);
  }
  .contact {
    position: absolute; left: 30px; width: 320px; top: 842px; text-align: center;
    font-size: 22px; line-height: 29.5px; color: var(--contact-grey);
  }
  .product { position: absolute; }
  .product-tray {
    left: -120px; top: 320px; width: 314px; height: 330px; border-radius: 50%;
    background: radial-gradient(circle at 55% 50%, var(--tray-tone) 0%, #cdae78 70%, var(--tray-dark) 100%);
  }
  .product-earrings {
    left: 534px; top: 140px; width: 120px; height: 250px; border-radius: 60px 0 0 60px;
    background: linear-gradient(180deg, rgba(214,181,90,0.55), rgba(214,181,90,0.85));
  }
  .product-slippers {
    left: 360px; top: 645px; width: 300px; height: 320px; border-radius: 140px 0 0 120px;
    background: linear-gradient(120deg, var(--slipper-cream) 0%, var(--slipper-pink) 40%, var(--slipper-lilac) 60%, var(--slipper-cream) 85%);
  }
</style>
</head>
<body>
<div class="canvas">
  <section class="invitation">
    <div class="footer-band"></div>

    <div class="brand-name">PELBRIKA</div>

    <div class="product product-earrings" role="img" aria-label="Product photo of gold beaded flower earrings with crystals"></div>
    <div class="product product-tray" role="img" aria-label="Product photo of a round leopard print lacquer tray"></div>
    <div class="product product-slippers" role="img" aria-label="Product photo of striped faux fur slide slippers in pink, cream and lilac"></div>

    <h1 class="event-title">Sip &amp; Shop</h1>

    <p class="event-details">THURSDAY, NOVEMBER 18<br>11 - 1 PM<br>478 FENWICK LANE</p>

    <p class="event-invite">COME ENJOY<br>SIPS, SNACKS AND SHOPPING!</p>

    <p class="event-blurb">Be the first to preview<br>our new winter collection and<br>get an early start<br>on your holiday gifting.</p>

    <p class="contact">Celia Marlow<br>info@pelbrika.com<br>402-319-5577</p>
  </section>
</div>
</body>
</html>
```